Treatment Info-Graphic Poster

22 x 28 poster. We need a design for a poster to hang in our treatment rooms that quickly compares different treatments we offer and sets expectations for the patient. Attached is something I very quickly created on Excel, but we would like one that matches our company colors and looks much more polished. I have attached a info-graphic we have had designed prior for reference.

Target Market(s)

Osteoarthritis of the knee patients treatment comparison info graphic for poster

Font styles to use
Serif

Colors
85cae6
f78f20

Requirements
Must have
• Branded treatment comparison table
Nice to have
• Treatment graphics

```html
<!DOCTYPE html>
<html lang="en">
<head>
<meta charset="utf-8">
<title>Knee OA Treatment Comparison</title>
<link href="https://fonts.googleapis.com/css2?family=Cinzel:wght@700&family=Fira+Sans+Condensed:wght@400;500;600&display=swap" rel="stylesheet">
<style>
:root{
  --brand-blue:#85cae6;
  --label-blue:#4f9bbb;
  --ha-blue:#7cbbd6;
  --stem-blue:#55a0c0;
  --title-blue:#4a88ad;
  --prp-orange:#e39a1e;
  --brace-orange:#c97a1b;
  --note-orange:#d98a1c;
  --stripe:#ebf3f2;
  --white:#ffffff;
}
*{margin:0;padding:0;box-sizing:border-box}
html,body{width:1200px;height:926px;overflow:hidden;background:var(--white)}
.poster{position:relative;width:1200px;height:926px;font-family:"Fira Sans Condensed",sans-serif;color:var(--white)}

.brand{position:absolute;left:48px;top:62px;width:234px;display:flex;align-items:center;gap:14px}
.brand-square{width:46px;height:46px;background:var(--brand-blue);border-radius:6px;flex:none}
.brand-name{font-size:50px;font-weight:500;line-height:1;color:var(--brand-blue)}
.brand-tagline{position:absolute;left:48px;width:234px;top:138px;text-align:center;font-size:21px;font-weight:400;color:var(--brand-blue)}
.brand-sub{position:absolute;left:48px;width:234px;top:218px;text-align:center;font-size:15px;font-weight:600;color:var(--title-blue);letter-spacing:.3px}

.title{position:absolute;left:336px;top:32px;width:826px;font-family:"Cinzel",serif;font-weight:700;color:var(--title-blue);font-size:66px;line-height:1;letter-spacing:2px;white-space:nowrap}
.subtitle{position:absolute;left:338px;top:98px;width:816px;display:flex;justify-content:space-between;font-family:"Cinzel",serif;font-weight:700;color:var(--title-blue);font-size:34px}

.heads{position:absolute;left:341px;top:150px;display:grid;grid-template-columns:repeat(4,201px);column-gap:3px}
.head{height:114px;border-radius:12px 12px 0 0;padding:8px 8px 0 10px;position:relative}
.head.ha{background:var(--ha-blue)}
.head.prp{background:var(--prp-orange)}
.head.stem{background:var(--stem-blue)}
.head.brace{background:var(--brace-orange)}
.head-name{font-size:15.5px;font-weight:500;line-height:17px;letter-spacing:.3px;height:34px}
.head-icon{position:absolute;right:18px;top:8px;width:30px;height:30px}
.head-grade{position:absolute;right:8px;top:40px;font-size:7.5px;font-weight:500}
.products{list-style:none;margin-top:14px;border-top:1px solid rgba(255,255,255,.6)}
.products li{display:flex;justify-content:space-between;font-size:7.6px;font-weight:500;line-height:13.5px;border-bottom:1px solid rgba(255,255,255,.45)}

.table{position:absolute;left:43px;top:264px;width:1111px}
.row{display:grid;grid-template-columns:298px repeat(4,124px 77px);height:52.6px}
.row > .label{background:var(--label-blue);border-radius:10px 0 0 10px;border-bottom:1px solid var(--white);display:flex;align-items:center;justify-content:space-between;padding:0 12px 0 21px;font-size:15.5px;font-weight:500;line-height:17px;letter-spacing:.2px}
.label svg{width:34px;height:34px;flex:none}
.row > span.cell{position:relative;border-bottom:1px solid rgba(255,255,255,.7)}
.row > span.cell.ha{background:var(--ha-blue)}
.row > span.cell.prp{background:var(--prp-orange)}
.row > span.cell.stem{background:var(--stem-blue)}
.row > span.cell.brace{background:var(--brace-orange)}
.cell::before,.cell::after{content:"";position:absolute;left:50%;top:50%;background:var(--white);transform:translate(-50%,-50%)}
.cell::before{width:20px;height:5px}
.cell::after{width:5px;height:20px}
.row.striped > span.empty{background:var(--stripe)}

.notice{position:absolute;left:43px;top:848px;width:1111px;height:54px}
.notice-bar{position:absolute;left:0;top:0;width:298px;height:54px;background:var(--prp-orange);border-radius:12px 0 0 12px}
.notice-mark{position:absolute;left:210px;top:0;width:88px;height:54px;background:var(--brace-orange);border-radius:12px 0 0 12px;border-left:4px solid var(--white);display:flex;align-items:center;justify-content:center;font-size:40px;font-weight:600;color:var(--white)}
.notice-text{position:absolute;left:309px;top:8px;font-size:14px;font-weight:500;line-height:20px;color:var(--note-orange);white-space:nowrap}
</style>
</head>
<body>
<div class="poster">

  <div class="brand">
    <span class="brand-square"></span>
    <span class="brand-name">kinetra</span>
  </div>
  <div class="brand-tagline">Move freely again</div>
  <div class="brand-sub">KNEE SPECIALISTS</div>

  <h1 class="title">KNEE OA TREATMENT</h1>
  <div class="subtitle"><span>C</span><span>O</span><span>M</span><span>P</span><span>A</span><span>R</span><span>I</span><span>S</span><span>O</span><span>N</span></div>

  <div class="heads">
    <div class="head ha">
      <div class="head-name">HYALURONIC<br>ACID (HA)</div>
      <svg class="head-icon" viewBox="0 0 30 30"><path d="M6 26 L10 22 M9 23 L22 8 L24 10 L11 25 Z M21 5 L27 11" stroke="#fff" stroke-width="2.4" fill="none" stroke-linecap="round"/></svg>
      <div class="head-grade">OA GRADE</div>
      <ul class="products">
        <li><span>SINGLE INJECTION (VISCORA)</span><span>1,2,3,4</span></li>
        <li><span>SINGLE INJECTION (LUBRIX)</span><span>1,2,3,4</span></li>
        <li><span>3 PART INJECTION SERIES (SYNOVEL)</span><span>1,2,3,4</span></li>
        <li><span>3/4 PART INJECTION SERIES (ARTIFLO)</span><span>1,2,3,4</span></li>
      </ul>
    </div>
    <div class="head prp">
      <div class="head-name">PLATELET RICH<br>PLASMA (PRP)</div>
      <svg class="head-icon" viewBox="0 0 30 30"><path d="M4 26 L9 21 M8 22 L21 9 L24 12 L11 25 Z M20 6 L27 13 M13 17 L15 19 M16 14 L18 16" stroke="#fff" stroke-width="2.2" fill="none" stroke-linecap="round"/></svg>
      <div class="head-grade">OA GRADE</div>
      <ul class="products">
        <li><span>SINGLE INJECTION (PLASMACEL)</span><span>1,2</span></li>
        <li><span>2 PART INJECTION SERIES</span><span>3,4</span></li>
      </ul>
    </div>
    <div class="head stem">
      <div class="head-name">STEM CELL<br>THERAPY &amp; PRP</div>
      <svg class="head-icon" viewBox="0 0 30 30"><path d="M4 26 L9 21 M8 22 L21 9 L24 12 L11 25 Z M20 6 L27 13 M5 4 Q11 8 5 12 M11 4 Q5 8 11 12" stroke="#fff" stroke-width="2" fill="none" stroke-linecap="round"/></svg>
      <div class="head-grade">OA GRADE</div>
      <ul class="products">
        <li><span>SINGLE INJECTION</span><span>1,2,3,4</span></li>
      </ul>
    </div>
    <div class="head brace">
      <div class="head-name">KNEE<br>BRACE(S)</div>
      <svg class="head-icon" viewBox="0 0 30 30"><rect x="12" y="3" width="8" height="11" rx="2" fill="#fff" transform="rotate(25 16 8)"/><rect x="8" y="16" width="7" height="12" rx="2" fill="#fff"/><circle cx="12" cy="15" r="3" fill="none" stroke="#fff" stroke-width="2"/></svg>
      <div class="head-grade">OA GRADE</div>
      <ul class="products">
        <li><span>STRIDEWELL 2</span><span>1,2,3,4</span></li>
        <li><span>PATELLAR STABILIZATION</span><span>1,2,3,4</span></li>
      </ul>
    </div>
  </div>

  <div class="table">
    <div class="row striped">
      <span class="label">CUSHION &amp;<br>LUBRICATE<svg viewBox="0 0 34 34"><path d="M6 18 L18 4 L30 14 L16 30 Z" fill="#fff"/><path d="M10 20 L22 26" stroke="#4f9bbb" stroke-width="2"/></svg></span>
      <span class="empty"></span><span class="cell ha"></span>
      <span class="empty"></span><span class="cell prp"></span>
      <span class="empty"></span><span class="cell stem"></span>
      <span class="empty"></span><span class="empty"></span>
    </div>
    <div class="row">
      <span class="label">DECREASE<br>INFLAMMATION<svg viewBox="0 0 34 34"><path d="M17 3 C22 10 28 15 26 23 C24 30 10 31 8 23 C6 16 12 14 12 9 C15 12 15 15 17 16 C19 12 18 8 17 3 Z" fill="#fff"/></svg></span>
      <span class="empty"></span><span class="cell ha"></span>
      <span class="empty"></span><span class="cell prp"></span>
      <span class="empty"></span><span class="cell stem"></span>
      <span class="empty"></span><span class="empty"></span>
    </div>
    <div class="row striped">
      <span class="label">STIMULATES SYNOVIAL<br>PRODUCTION OF HA<svg viewBox="0 0 34 34"><rect x="12" y="2" width="10" height="13" rx="4" fill="#fff"/><rect x="11" y="18" width="11" height="14" rx="4" fill="#fff"/></svg></span>
      <span class="empty"></span><span class="cell ha"></span>
      <span class="empty"></span><span class="cell prp"></span>
      <span class="empty"></span><span class="cell stem"></span>
      <span class="empty"></span><span class="empty"></span>
    </div>
    <div class="row">
      <span class="label">HEALING<br>PROPERTIES<svg viewBox="0 0 34 34"><path d="M17 30 L5 18 C0 12 5 4 11 5 C14 5 16 8 17 10 C18 8 20 5 23 5 C29 4 34 12 29 18 Z" fill="#fff"/><path d="M20 17 h8 M24 13 v8" stroke="#4f9bbb" stroke-width="2.5"/></svg></span>
      <span class="empty"></span><span class="empty"></span>
      <span class="empty"></span><span class="cell prp"></span>
      <span class="empty"></span><span class="cell stem"></span>
      <span class="empty"></span><span class="empty"></span>
    </div>
    <div class="row striped">
      <span class="label">REPAIRATIVE<br>PROPERTIES<svg viewBox="0 0 34 34"><circle cx="17" cy="17" r="12" fill="none" stroke="#fff" stroke-width="4"/><circle cx="17" cy="17" r="5" fill="#fff"/></svg></span>
      <span class="empty"></span><span class="empty"></span>
      <span class="empty"></span><span class="empty"></span>
      <span class="empty"></span><span class="cell stem"></span>
      <span class="empty"></span><span class="empty"></span>
    </div>
    <div class="row">
      <span class="label">POTENTIAL CARTILAGE<br>REGENERATION<svg viewBox="0 0 34 34"><rect x="12" y="2" width="10" height="13" rx="4" fill="#fff"/><rect x="11" y="18" width="11" height="14" rx="4" fill="#fff"/></svg></span>
      <span class="empty"></span><span class="empty"></span>
      <span class="empty"></span><span class="empty"></span>
      <span class="empty"></span><span class="cell stem"></span>
      <span class="empty"></span><span class="empty"></span>
    </div>
    <div class="row striped">
      <span class="label">ON AVERAGE,<br>BENEFITS LAST 4-6 MONTHS<svg viewBox="0 0 34 34"><path d="M17 4 A13 13 0 1 1 5 21" fill="none" stroke="#a9d2e4" stroke-width="2.5"/><path d="M17 10 A7 7 0 1 1 11 20" fill="none" stroke="#fff" stroke-width="3"/></svg></span>
      <span class="empty"></span><span class="cell ha"></span>
      <span class="empty"></span><span class="cell prp"></span>
      <span class="empty"></span><span class="cell stem"></span>
      <span class="empty"></span><span class="cell brace"></span>
    </div>
    <div class="row">
      <span class="label">ON AVERAGE,<br>BENEFITS LAST 6-12 MONTHS<svg viewBox="0 0 34 34"><path d="M17 4 A13 13 0 1 1 5 21" fill="none" stroke="#fff" stroke-width="2.5"/><path d="M17 10 A7 7 0 1 1 11 20" fill="none" stroke="#fff" stroke-width="3"/></svg></span>
      <span class="empty"></span><span class="empty"></span>
      <span class="empty"></span><span class="cell prp"></span>
      <span class="empty"></span><span class="cell stem"></span>
      <span class="empty"></span><span class="cell brace"></span>
    </div>
    <div class="row striped">
      <span class="label">ON AVERAGE,<br>BENEFITS LAST 18+ MONTHS<svg viewBox="0 0 34 34"><path d="M17 3 A14 14 0 1 1 3 17 A10 10 0 0 1 13 7 A7 7 0 1 1 11 22" fill="none" stroke="#fff" stroke-width="3"/></svg></span>
      <span class="empty"></span><span class="empty"></span>
      <span class="empty"></span><span class="empty"></span>
      <span class="empty"></span><span class="cell stem"></span>
      <span class="empty"></span><span class="cell brace"></span>
    </div>
    <div class="row">
      <span class="label">CORRECTS BIOMECHANICS<br>&amp; STABILIZES JOINT<svg viewBox="0 0 34 34"><path d="M12 4 v26 M8 8 h8 M12 14 h10 v14 h-10" fill="none" stroke="#fff" stroke-width="3.5"/></svg></span>
      <span class="empty"></span><span class="empty"></span>
      <span class="empty"></span><span class="empty"></span>
      <span class="empty"></span><span class="empty"></span>
      <span class="empty"></span><span class="cell brace"></span>
    </div>
    <div class="row striped">
      <span class="label">COVERED<br>BY MOST INSURANCE<svg viewBox="0 0 34 34"><path d="M6 10 L14 4 H28 V30 H6 Z" fill="#fff"/><path d="M11 14 h13 M11 18 h13 M11 22 h13 M11 26 h13" stroke="#4f9bbb" stroke-width="1.2"/></svg></span>
      <span class="empty"></span><span class="cell ha"></span>
      <span class="empty"></span><span class="empty"></span>
      <span class="empty"></span><span class="empty"></span>
      <span class="empty"></span><span class="cell brace"></span>
    </div>
  </div>

  <div class="notice">
    <div class="notice-bar"></div>
    <div class="notice-mark">!</div>
    <p class="notice-text">Treatment outcomes vary by individual. Treatment benefits and length of efficacy are not guaranteed.<br>In some cases, patient’s do not respond to treatment. Multiple treatments may be recommended or necessary for the best outcomes.</p>
  </div>

</div>
</body>
</html>
```